Frostwyn.co - Polar Expeditions Specialists

We need a modern, visually striking business card for Frostwyn.co, a company specialized in selling expedition cruises to the most remote regions on Earth, with a focus on the Arctic and Antarctica. The design should instantly communicate that the cardholder is an expert in polar travel. Use clean, premium aesthetics with cool tones like icy blue and white, possibly incorporating polar imagery (ice, glaciers, penguins, etc.)

Attached the logo

Contact Information for Business Card

Feels high-end and trustworthy.. Visually memorable — encourages people to keep it

Colors
0054AA
0677BA
7BADD7
CADEEF
E8F1F8

Requirements
Must have
• ice, glaciers, penguins, montains
Nice to have
• modern, transparente,

```html
<!DOCTYPE html>
<html lang="en">
<head>
<meta charset="UTF-8">
<title>Frostwyn.co – Business Card</title>
<link href="https://fonts.googleapis.com/css2?family=Poppins:wght@400;600;700&display=swap" rel="stylesheet">
<style>
  :root {
    --stage: #e2e2e2;
    --paper: #ffffff;
    --brand-blue: #3a78c0;
    --edge-blue: #3b7fd0;
    --navy-deep: #15213f;
    --navy: #26365a;
    --ice-tone: #4a5b7e;
    --text-grey: #6b6b6b;
    --white: #ffffff;
  }
  * { margin: 0; padding: 0; box-sizing: border-box; }
  html, body { width: 1200px; height: 791px; overflow: hidden; }
  body {
    background: var(--stage);
    font-family: "Poppins", sans-serif;
    display: flex;
    align-items: center;
    justify-content: center;
    gap: 48px;
  }
  .card {
    width: 530px;
    height: 303px;
    border-radius: 3px;
    border-bottom: 3px solid var(--edge-blue);
    box-shadow: 0 10px 24px rgba(0,0,0,0.18);
    position: relative;
    overflow: hidden;
  }
  /* Front side */
  .card-front { background: var(--paper); }
  .brand-lockup {
    position: absolute;
    top: 64px;
    left: 0; right: 0;
    display: flex;
    align-items: center;
    justify-content: center;
    gap: 14px;
  }
  .brand-dot {
    width: 58px; height: 58px;
    border-radius: 50%;
    background: var(--brand-blue);
    flex-shrink: 0;
  }
  .brand-text { display: flex; flex-direction: column; }
  .brand-name {
    font-weight: 700;
    font-size: 44px;
    line-height: 1;
    color: var(--brand-blue);
  }
  .brand-tagline {
    font-weight: 600;
    font-size: 12.5px;
    color: var(--brand-blue);
    margin-top: 6px;
    letter-spacing: 0.1px;
  }
  .details-row {
    position: absolute;
    left: 0; right: 0;
    bottom: 54px;
    display: flex;
    align-items: center;
    justify-content: center;
    gap: 26px;
  }
  .holder { text-align: right; }
  .holder-name {
    font-weight: 700;
    font-size: 20px;
    color: var(--brand-blue);
    letter-spacing: 0.3px;
  }
  .holder-role {
    font-size: 13px;
    color: var(--text-grey);
  }
  .divider {
    width: 1.5px;
    height: 66px;
    background: var(--brand-blue);
  }
  .contact-list { list-style: none; }
  .contact-item {
    display: flex;
    align-items: center;
    gap: 8px;
    font-size: 13px;
    color: var(--text-grey);
    line-height: 1.6;
  }
  .contact-item svg { width: 12px; height: 12px; fill: var(--brand-blue); flex-shrink: 0; }

  /* Back side */
  .card-back {
    background: var(--navy);
    display: flex;
    align-items: center;
    justify-content: center;
  }
  .back-scene {
    position: absolute;
    inset: 0;
    background:
      radial-gradient(ellipse at 40% 70%, var(--ice-tone) 0%, transparent 55%),
      linear-gradient(180deg, var(--navy) 0%, var(--navy) 45%, var(--navy-deep) 100%);
  }
  .back-lockup {
    position: relative;
    display: flex;
    flex-direction: column;
    align-items: center;
  }
  .back-dot {
    width: 70px; height: 70px;
    border-radius: 50%;
    background: var(--white);
    margin-bottom: 14px;
  }
  .back-name {
    font-weight: 700;
    font-size: 54px;
    line-height: 1;
    color: var(--white);
  }
  .back-tagline {
    font-weight: 600;
    font-size: 15px;
    color: var(--white);
    margin-top: 8px;
  }
</style>
</head>
<body>
  <section class="card card-front">
    <div class="brand-lockup">
      <span class="brand-dot"></span>
      <div class="brand-text">
        <span class="brand-name">Frostwyn.co</span>
        <span class="brand-tagline">Polar Expeditions Specialists</span>
      </div>
    </div>
    <div class="details-row">
      <div class="holder">
        <div class="holder-name">MARCUS VELL</div>
        <div class="holder-role">President</div>
      </div>
      <span class="divider"></span>
      <ul class="contact-list">
        <li class="contact-item">
          <svg viewBox="0 0 24 24"><path d="M6.6 10.8a15.1 15.1 0 0 0 6.6 6.6l2.2-2.2a1 1 0 0 1 1-.25 11.4 11.4 0 0 0 3.6.57 1 1 0 0 1 1 1V20a1 1 0 0 1-1 1A17 17 0 0 1 3 4a1 1 0 0 1 1-1h3.5a1 1 0 0 1 1 1c0 1.25.2 2.45.57 3.6a1 1 0 0 1-.25 1z"/></svg>
          555-301-7782
        </li>
        <li class="contact-item">
          <svg viewBox="0 0 24 24"><path d="M2 5h20v14H2z M2 5l10 8 10-8" stroke="#fff" stroke-width="1.5"/></svg>
          marcusvell@frostwyn.co
        </li>
        <li class="contact-item">
          <svg viewBox="0 0 24 24"><circle cx="12" cy="12" r="10"/><path d="M2 12h20M12 2c3 3 3 17 0 20M12 2c-3 3-3 17 0 20" stroke="#fff" stroke-width="1.3" fill="none"/></svg>
          www.frostwyn.co
        </li>
      </ul>
    </div>
  </section>

  <section class="card card-back">
    <div class="back-scene" role="img" aria-label="Dusky navy photograph of icebergs floating on a calm polar sea"></div>
    <div class="back-lockup">
      <span class="back-dot"></span>
      <span class="back-name">Frostwyn.co</span>
      <span class="back-tagline">Polar Expeditions Specialists</span>
    </div>
  </section>
</body>
</html>
```